Fashion Label Startup Business Card Design

Maribel Quint is a startup fashion designer based on the Gold Coast in QLD Australia. Maribels label " Vorine by Quint " is based upon taking old world design techniques and infusing them modern twist. The card design should incorporate an old world theme using colours like mustard, ocha, black, white and elements of lace pattern.

Card Details:

Maribel Quint
Fashion Designer
P: 04 0152 6847
E: vorinebyquint@mailbrook.com
W: www.friendsnet.com/VOrineByQuint

```html
<!DOCTYPE html>
<html lang="en">
<head>
<meta charset="utf-8">
<title>Maribel Quint — Fashion Designer Business Card</title>
<link rel="stylesheet" href="https://fonts.googleapis.com/css2?family=Jura:wght@300&family=Oxanium:wght@600&family=Open+Sans:wght@400&display=swap">
<style>
  :root {
    --paper-olive: #9c9a72;
    --paper-grey: #8f8d7e;
    --paper-light: #c9c48a;
    --mustard-deep: #8a6a1e;
    --mustard: #b89a3a;
    --chevron-grey: #7f7f7a;
    --chevron-light: #9a9a92;
    --ink: #111111;
    --contact-blue: #2b2bd6;
    --edge-yellow: #d8d25a;
  }
  html, body {
    margin: 0;
    padding: 0;
    overflow: hidden;
    background: #ffffff;
  }
  .business-card {
    display: block;
    width: 1200px;
    height: 678px;
  }
  .role-title {
    font-family: "Jura", sans-serif;
    font-weight: 300;
    font-size: 50px;
    letter-spacing: 2px;
    fill: var(--ink);
  }
  .designer-name {
    font-family: "Oxanium", sans-serif;
    font-weight: 600;
    font-size: 96px;
    fill: var(--ink);
  }
  .contact-line {
    font-family: "Open Sans", sans-serif;
    font-size: 27px;
    fill: var(--contact-blue);
  }
</style>
</head>
<body>
<svg class="business-card" viewBox="0 0 1200 678" xmlns="http://www.w3.org/2000/svg">
  <defs>
    <linearGradient id="paper-tone" x1="0" y1="0" x2="1" y2="0.6">
      <stop offset="0" stop-color="var(--paper-grey)"/>
      <stop offset="0.55" stop-color="var(--paper-olive)"/>
      <stop offset="1" stop-color="var(--paper-light)"/>
    </linearGradient>
    <linearGradient id="mustard-tone" x1="0" y1="1" x2="1" y2="0">
      <stop offset="0" stop-color="var(--mustard-deep)"/>
      <stop offset="0.6" stop-color="var(--mustard)"/>
      <stop offset="1" stop-color="var(--paper-light)"/>
    </linearGradient>
  </defs>

  <g class="card-background" role="img" aria-label="Aged paper texture in olive, grey and mustard tones">
    <rect width="1200" height="678" fill="url(#paper-tone)"/>
    <polygon class="mustard-field" points="0,620 1200,20 1200,678 0,678" fill="url(#mustard-tone)" opacity="0.75"/>
  </g>

  <g class="chevron-mark">
    <polygon class="chevron-back" points="330,350 1195,12 1090,340 520,470" fill="var(--chevron-light)" opacity="0.55"/>
    <polygon class="chevron-front" points="210,320 490,462 1185,14 600,360 380,330" fill="var(--chevron-grey)" opacity="0.8"/>
  </g>

  <rect class="card-edge" x="1" y="1" width="1198" height="676" fill="none" stroke="var(--edge-yellow)" stroke-width="2"/>

  <text class="role-title" x="44" y="170">Fashion Designer</text>
  <text class="designer-name" x="666" y="278" text-anchor="end">Maribel</text>
  <text class="designer-name" x="666" y="374" text-anchor="end">QUINT</text>

  <g class="contact-details" text-anchor="end">
    <text class="contact-line" x="1160" y="544">04 0152 6847</text>
    <text class="contact-line" x="1160" y="594">vorinebyquint@mailbrook.com</text>
    <text class="contact-line" x="1160" y="642">www.friendsnet.com/VOrineByQuint</text>
  </g>
</svg>
</body>
</html>
```